Web Site Design and Business Card design for Recruiting Company

There are three major tasks in this project:
1) I need to re-design my newly created website www.talvexhire.net using the same logo but creating a totally different recruiting template that will apply better for a recruitment site. I want to use the elements of the Talvex Hiring Network logo (which is the road junction) and red, black and gray colors throughout the website. I need someone to both design and launch the site...
2) I would also like to design a double sided business card using the same logo/colors and elements as described above
3) I would also like to have a small thumbnail logo created. As our large logo cannot be previewed easily on the Corvanet or on Pelmora Vista tab images

The design should be contemporary, minimalist and slick

```html
<!DOCTYPE html>
<html lang="en">
<head>
<meta charset="utf-8">
<title>Talvex Hiring Network</title>
<link rel="stylesheet" href="https://fonts.googleapis.com/css2?family=Roboto:wght@300;400;500;700&family=Roboto+Slab:wght@400;700&display=swap">
<style>
:root{
  --red:#e0102a;
  --red-dark:#b50a1f;
  --ink:#1c1c1c;
  --charcoal:#2b2b2b;
  --grey-card:#9b9b9b;
  --white:#ffffff;
  --text:#444444;
  --muted:#b5b5b5;
}
*{box-sizing:border-box;margin:0;padding:0}
html,body{width:1200px;height:3080px;overflow:hidden}
body{position:relative;background:var(--white);font-family:"Roboto",sans-serif;color:var(--text)}
.abs{position:absolute}

/* header */
.site-header{left:0;top:0;width:1200px;height:160px;background:var(--white)}
.brand{left:170px;top:40px;display:flex;align-items:center;gap:12px}
.brand-mark{width:26px;height:26px;background:var(--red)}
.brand-name{font-weight:700;font-size:24px;color:var(--charcoal);line-height:1.1;width:170px}
.topbar{right:170px;top:42px;display:flex;align-items:center;gap:14px}
.social-dot{width:12px;height:12px;border-radius:50%;background:var(--charcoal)}
.call{display:flex;align-items:center;gap:10px;margin-left:14px;font-size:21px;color:var(--charcoal)}
.call-icon{width:30px;height:30px;border-radius:50%;background:var(--red);display:flex;align-items:center;justify-content:center}
.main-nav{right:170px;top:108px;display:flex;align-items:center;gap:46px;font-size:17px;color:var(--charcoal)}
.main-nav .active{color:var(--red);border-bottom:2px solid var(--red);padding-bottom:6px}

/* hero */
.hero{left:0;top:160px;width:1200px;height:580px;background:radial-gradient(ellipse at 50% 0%,#e2e2e2 0%,#b9b5b0 50%,#5f5a56 100%)}
.hero-title{left:0;top:378px;width:1200px;text-align:center;font-family:"Roboto Slab",serif;font-weight:700;font-size:40px;color:var(--white)}
.hero-btn{left:495px;top:448px;width:210px;height:50px;border-radius:25px;background:var(--red);color:var(--white);font-weight:700;font-size:18px;display:flex;align-items:center;justify-content:center}

/* welcome */
.welcome-title{left:0;top:820px;width:1200px;text-align:center;font-family:"Roboto Slab",serif;font-weight:400;font-size:40px;color:var(--ink)}
.hex{top:912px;width:270px;height:300px}
.hex-shape{position:absolute;inset:0}
.hex-body{position:absolute;inset:0;display:flex;flex-direction:column;align-items:center;padding-top:56px}
.hex-label{margin-top:18px;color:var(--white);font-size:19px;letter-spacing:.5px}
.hex-sub{margin-top:6px;color:#9a9a9a;font-size:12px}
.hex-btn{margin-top:26px;padding:6px 16px;border:1px solid #bbb;border-radius:14px;color:var(--white);font-size:12px}

/* about */
.about-band{left:0;top:1370px;width:1200px;height:640px;background:linear-gradient(180deg,var(--red),var(--red-dark));clip-path:polygon(0 0,100% 0,100% 88%,0 100%)}
.about-title{left:172px;top:1520px;font-family:"Roboto Slab",serif;font-weight:400;font-size:36px;color:var(--white)}
.about-text{left:172px;top:1585px;width:400px;font-size:15px;line-height:1.6;color:var(--white)}
.about-photo{left:640px;top:1460px;width:370px;height:370px;border-radius:50%;border:10px solid var(--white);background:radial-gradient(circle at 45% 40%,#e8e6e3 0%,#b8b3ae 55%,#5c5651 100%)}

/* services */
.services-title{left:0;top:2030px;width:1200px;text-align:center;font-family:"Roboto Slab",serif;font-weight:400;font-size:40px;color:var(--ink)}
.services-sub{left:0;top:2086px;width:1200px;text-align:center;font-size:17px;line-height:1.5;color:var(--text)}
.card{top:2164px;width:276px;height:400px;background:var(--white);box-shadow:0 2px 10px rgba(0,0,0,.18)}
.card-head{height:76px;display:flex;align-items:center;justify-content:space-between;padding:0 16px;color:var(--white);font-size:17px;line-height:1.25;background:var(--grey-card)}
.card-head.red{background:var(--red)}
.card-list{list-style:none;padding:18px 0 0 18px}
.card-list li{font-size:12.5px;line-height:25px;color:var(--text)}
.card-list li::before{content:"";display:inline-block;width:5px;height:5px;border-radius:50%;background:var(--charcoal);margin-right:10px;vertical-align:middle}
.card-btn{position:absolute;left:18px;bottom:-14px;width:110px;height:32px;border-radius:16px;background:var(--red);color:var(--white);font-size:13px;display:flex;align-items:center;justify-content:center}

/* footer */
.site-footer{left:0;top:2690px;width:1200px;height:390px;background:linear-gradient(180deg,#262626,#101010);clip-path:polygon(0 8%,100% 0,100% 100%,0 100%)}
.contact{top:2780px;width:240px;text-align:center;color:var(--white)}
.contact-icon{width:66px;height:66px;margin:0 auto 12px;border-radius:50%;border:3px solid var(--red);display:flex;align-items:center;justify-content:center}
.contact-label{font-size:17px;font-weight:700}
.contact-detail{margin-top:6px;font-size:12.5px;line-height:1.6;color:var(--muted)}
.contact-detail.strong{color:var(--red);font-size:15px;font-weight:500}
.copyright{left:0;top:3046px;width:1200px;text-align:center;font-size:12px;color:#a0a0a0}
</style>
</head>
<body>

<header class="abs site-header">
  <div class="abs brand"><span class="brand-mark"></span><span class="brand-name">Talvex Hiring Network</span></div>
  <div class="abs topbar">
    <span class="social-dot"></span><span class="social-dot"></span><span class="social-dot"></span><span class="social-dot"></span><span class="social-dot"></span>
    <span class="call"><span class="call-icon"><svg width="16" height="16" viewBox="0 0 24 24"><path fill="#fff" d="M6.6 10.8a15 15 0 0 0 6.6 6.6l2.2-2.2a1 1 0 0 1 1-.25 11.4 11.4 0 0 0 3.6.57 1 1 0 0 1 1 1V20a1 1 0 0 1-1 1A17 17 0 0 1 3 4a1 1 0 0 1 1-1h3.5a1 1 0 0 1 1 1c0 1.25.2 2.45.57 3.57a1 1 0 0 1-.25 1z"/></svg></span>Call Us: +1-555-014-0636</span>
  </div>
  <nav class="abs main-nav">
    <span class="active">Home</span><span>About Us</span><span>Services</span><span>Contact Us</span>
    <svg width="16" height="16" viewBox="0 0 24 24"><circle cx="10" cy="10" r="7" fill="none" stroke="#2b2b2b" stroke-width="3"/><path d="M15 15l6 6" stroke="#2b2b2b" stroke-width="3"/></svg>
  </nav>
</header>

<section>
  <div class="abs hero" role="img" aria-label="Photo of recruiters interviewing a candidate across an office table"></div>
  <h1 class="abs hero-title">Talvex Hiring Network</h1>
  <div class="abs hero-btn">Get Started Here!</div>
</section>

<section>
  <h2 class="abs welcome-title">Welcome to Talvex Hiring Network</h2>

  <div class="abs hex" style="left:165px">
    <svg class="hex-shape" viewBox="0 0 270 300"><polygon points="135,6 264,78 264,222 135,294 6,222 6,78" fill="#2b2b2b" stroke="#e0102a" stroke-width="6"/></svg>
    <div class="hex-body">
      <svg width="74" height="74" viewBox="0 0 74 74"><circle cx="30" cy="30" r="20" fill="none" stroke="#e0102a" stroke-width="6"/><path d="M45 45l20 20" stroke="#e0102a" stroke-width="8" stroke-linecap="round"/></svg>
      <div class="hex-label">JOB SEARCH</div>
      <div class="hex-sub">Find roles that fit you</div>
      <div class="hex-btn">Read More</div>
    </div>
  </div>

  <div class="abs hex" style="left:465px">
    <svg class="hex-shape" viewBox="0 0 270 300"><polygon points="135,6 264,78 264,222 135,294 6,222 6,78" fill="#2b2b2b" stroke="#e0102a" stroke-width="6"/></svg>
    <div class="hex-body">
      <svg width="74" height="74" viewBox="0 0 74 74"><circle cx="37" cy="22" r="13" fill="none" stroke="#e0102a" stroke-width="5"/><path d="M12 68c0-16 11-26 25-26s25 10 25 26" fill="none" stroke="#e0102a" stroke-width="5"/><rect x="30" y="48" width="14" height="10" fill="#e0102a"/></svg>
      <div class="hex-label">EMPLOYERS</div>
      <div class="hex-sub">Hire skilled professionals</div>
      <div class="hex-btn">Read More</div>
    </div>
  </div>

  <div class="abs hex" style="left:765px">
    <svg class="hex-shape" viewBox="0 0 270 300"><polygon points="135,6 264,78 264,222 135,294 6,222 6,78" fill="#2b2b2b" stroke="#e0102a" stroke-width="6"/></svg>
    <div class="hex-body">
      <svg width="74" height="74" viewBox="0 0 74 74"><circle cx="22" cy="24" r="9" fill="none" stroke="#e0102a" stroke-width="4"/><circle cx="52" cy="24" r="9" fill="none" stroke="#e0102a" stroke-width="4"/><path d="M6 62c0-12 7-20 16-20s16 8 16 20M36 62c0-12 7-20 16-20s16 8 16 20" fill="none" stroke="#e0102a" stroke-width="4"/></svg>
      <div class="hex-label">CANDIDATES</div>
      <div class="hex-sub">Grow your career path</div>
      <div class="hex-btn">Read More</div>
    </div>
  </div>
</section>

<section>
  <div class="abs about-band"></div>
  <h2 class="abs about-title">About Us</h2>
  <p class="abs about-text">Talvex Hiring Network LLC is an Atlanta based talent advisory, recruiting and staffing firm. We help companies find skilled professionals within the shortest time frame through our unique network of business and personal connections nationwide and overseas.</p>
  <div class="abs about-photo" role="img" aria-label="Photo of a smiling businesswoman at a desk"></div>
</section>

<section>
  <h2 class="abs services-title">Services</h2>
  <p class="abs services-sub">We specialize in sourcing, recruiting, placement and staffing<br>of candidates in the following categories:</p>

  <div class="abs card" style="left:170px">
    <div class="card-head">Information<br>Technology (IT)
      <svg width="30" height="24" viewBox="0 0 30 24"><rect x="2" y="2" width="26" height="16" fill="none" stroke="#fff" stroke-width="2"/><path d="M10 22h10" stroke="#fff" stroke-width="2"/></svg>
    </div>
    <ul class="card-list">
      <li>Project Management</li><li>Web and Application Development</li><li>Network Administration</li><li>Mobile Development</li><li>Quality Assurance</li><li>ERP and CRM Consulting</li><li>Business Intelligence (BI)</li><li>Big Data Analytics</li><li>Reporting and Data Visualization</li>
    </ul>
    <div class="card-btn">Read More</div>
  </div>

  <div class="abs card" style="left:462px">
    <div class="card-head red">Telecommunications
      <svg width="24" height="28" viewBox="0 0 24 28"><path d="M12 4v22M5 26l7-22 7 22M7 16h10" fill="none" stroke="#fff" stroke-width="2"/></svg>
    </div>
    <ul class="card-list">
      <li>Project Management</li><li>Construction Management</li><li>Site Acquisition</li><li>Land Installation and Civil Work</li><li>RF Engineering and Network Design</li><li>Cell Site Integration</li><li>Network Optimization</li><li>Site Maintenance</li><li>Quality Assurance</li>
    </ul>
    <div class="card-btn">Read More</div>
  </div>

  <div class="abs card" style="left:754px">
    <div class="card-head">Accounting &amp;<br>Finance
      <svg width="28" height="24" viewBox="0 0 28 24"><path d="M3 22h22M6 20v-6M12 20v-10M18 20v-8M24 20v-14" stroke="#fff" stroke-width="3"/></svg>
    </div>
    <ul class="card-list">
      <li>Financial Planning</li><li>Financial Management</li><li>Certified Public Accounting (CPA)</li><li>Audit</li><li>Cost Accounting</li><li>Accounts Receivable</li><li>Accounts Payable</li><li>Business Analysis</li><li>Credit and Collections</li>
    </ul>
    <div class="card-btn">Read More</div>
  </div>
</section>

<footer>
  <div class="abs site-footer"></div>

  <div class="abs contact" style="left:260px">
    <div class="contact-icon"><svg width="28" height="22" viewBox="0 0 28 22"><rect x="2" y="2" width="24" height="18" fill="none" stroke="#fff" stroke-width="2"/><path d="M2 3l12 9 12-9" fill="none" stroke="#fff" stroke-width="2"/></svg></div>
    <div class="contact-label">Email</div>
    <div class="contact-detail">info@talvexhire.net<br>hr@talvexhire.net</div>
  </div>

  <div class="abs contact" style="left:480px">
    <div class="contact-icon"><svg width="26" height="26" viewBox="0 0 24 24"><path fill="#fff" d="M6.6 10.8a15 15 0 0 0 6.6 6.6l2.2-2.2a1 1 0 0 1 1-.25 11.4 11.4 0 0 0 3.6.57 1 1 0 0 1 1 1V20a1 1 0 0 1-1 1A17 17 0 0 1 3 4a1 1 0 0 1 1-1h3.5a1 1 0 0 1 1 1c0 1.25.2 2.45.57 3.57a1 1 0 0 1-.25 1z"/></svg></div>
    <div class="contact-label">Phone</div>
    <div class="contact-detail strong">+1-555-014-0636</div>
  </div>

  <div class="abs contact" style="left:690px">
    <div class="contact-icon"><svg width="28" height="28" viewBox="0 0 28 28"><circle cx="14" cy="14" r="11" fill="none" stroke="#fff" stroke-width="2"/><path d="M14 7v7l5 3" fill="none" stroke="#fff" stroke-width="2"/></svg></div>
    <div class="contact-label">Hours</div>
    <div class="contact-detail">Mon - Fri: 8:00 AM - 6:00 PM<br>Sat: 10:00 AM - 4:00 PM<br>Sun: Closed</div>
  </div>

  <p class="abs copyright">Copyright © 2020 Talvex Hiring Network. All Rights Reserved. Sitemap</p>
</footer>

</body>
</html>
```